Business card design for event company

need design double sided in square shape ( approx 6x6cm) in matt grey shades
front side :
logo ( could be in one color like picture attached ) printpress effect in a rect box

back side :
name in big font with silver foil finish ( similar to attached pic )

phone number i would like to see how it will look like if embossed ( like in credit cards )

Sample for contact on card ( will need 5 different contacts) - pls. include small icons next to each contact

WALEED RAFIQI
Managing Director

+971 50 317 6490
waleed@loomcrestuae.com
www.loomcrest.ae
Building C2 , Office 713
Dubai Saffron Heights

Please consider this is an urgent project . thank you in advance

```html
<!DOCTYPE html>
<html lang="en">
<head>
<meta charset="utf-8">
<title>Loomcrest – Business Card</title>
<link rel="stylesheet" href="https://fonts.googleapis.com/css2?family=Lato:wght@300;400;700;900&display=swap">
<style>
  :root {
    --backdrop: #2a2a2a;
    --card: #1b1b1b;
    --gold: #e2b325;
    --gold-light: #f7dc6a;
    --gold-deep: #a97c12;
    --ink-light: #f2f2f2;
  }
  * { box-sizing: border-box; margin: 0; padding: 0; }
  html, body {
    width: 1200px; height: 900px; overflow: hidden;
    background: var(--backdrop);
    font-family: "Lato", Arial, sans-serif;
  }
  .canvas {
    width: 1200px; height: 900px;
    display: flex; align-items: center; justify-content: center; gap: 60px;
  }
  .card {
    position: relative;
    width: 440px; height: 440px;
    background: var(--card);
    border-radius: 8px;
    box-shadow: 0 14px 30px rgba(0,0,0,.45);
  }
  .card-frame {
    position: absolute; inset: 20px;
    border: 3px solid var(--gold);
    border-image: linear-gradient(135deg, var(--gold-light), var(--gold), var(--gold-deep), var(--gold-light)) 1;
  }

  /* Front */
  .brand {
    position: absolute; left: 0; right: 0; top: 150px;
    display: flex; align-items: center; justify-content: center; gap: 14px;
  }
  .brand-mark {
    width: 18px; height: 18px; background: var(--gold);
  }
  .brand-name {
    font-size: 46px; font-weight: 700; color: var(--gold);
    letter-spacing: 1px;
  }
  .website {
    position: absolute; left: 0; right: 0; bottom: 62px;
    text-align: center;
    font-size: 13px; font-weight: 700; letter-spacing: 4px;
    color: var(--gold);
  }

  /* Back */
  .holder-name {
    position: absolute; left: 44px; right: 44px; top: 58px;
    font-size: 35px; color: var(--gold); letter-spacing: 1px;
    white-space: nowrap; text-align: right;
  }
  .holder-name .given { font-weight: 300; }
  .holder-name .family { font-weight: 900; color: var(--gold-light); }
  .role-row {
    position: absolute; left: 44px; right: 44px; top: 112px;
    display: flex; align-items: center; gap: 10px;
  }
  .role-row .rule { flex: 1; height: 1px; background: var(--ink-light); }
  .role-title {
    font-size: 12px; font-weight: 700; letter-spacing: 2.5px; color: var(--ink-light);
  }
  .contacts {
    position: absolute; left: 52px; bottom: 70px;
    list-style: none; color: var(--ink-light);
    font-size: 16px; line-height: 1.4;
  }
  .contacts li { display: flex; align-items: flex-start; gap: 12px; margin-top: 6px; }
  .contacts svg { width: 14px; height: 14px; margin-top: 3px; flex: none; fill: var(--ink-light); }
  .contacts .phone { font-weight: 700; letter-spacing: 1px; }
</style>
</head>
<body>
<main class="canvas">

  <section class="card card-front" aria-label="Card front">
    <div class="card-frame"></div>
    <div class="brand">
      <span class="brand-mark"></span>
      <span class="brand-name">Loomcrest</span>
    </div>
    <p class="website">www.loomcrest.ae</p>
  </section>

  <section class="card card-back" aria-label="Card back">
    <div class="card-frame"></div>
    <h1 class="holder-name"><span class="given">WALEED</span> <span class="family">RAFIQI</span></h1>
    <div class="role-row">
      <span class="rule"></span>
      <span class="role-title">Managing Director</span>
      <span class="rule" style="flex:0 0 40px"></span>
    </div>
    <ul class="contacts">
      <li>
        <svg viewBox="0 0 24 24" aria-hidden="true"><path d="M6.6 10.8a15.1 15.1 0 0 0 6.6 6.6l2.2-2.2c.3-.3.7-.4 1-.2 1.1.4 2.3.6 3.6.6.6 0 1 .4 1 1V20c0 .6-.4 1-1 1C10.6 21 3 13.4 3 4c0-.6.4-1 1-1h3.5c.6 0 1 .4 1 1 0 1.3.2 2.5.6 3.6.1.3 0 .7-.2 1z"/></svg>
        <span class="phone">+971 50 317 6490</span>
      </li>
      <li>
        <svg viewBox="0 0 24 24" aria-hidden="true"><path d="M2 5h20v14H2zm2 2v.5l8 5 8-5V7zm0 2.8V17h16V9.8l-8 5z"/></svg>
        <span>waleed@loomcrestuae.com</span>
      </li>
      <li>
        <svg viewBox="0 0 24 24" aria-hidden="true"><path d="M12 2a7 7 0 0 0-7 7c0 5.2 7 13 7 13s7-7.8 7-13a7 7 0 0 0-7-7zm0 9.5A2.5 2.5 0 1 1 12 6.5a2.5 2.5 0 0 1 0 5z"/></svg>
        <span>Building C2 , Office 713<br>Dubai Saffron Heights</span>
      </li>
    </ul>
  </section>

</main>
</body>
</html>
```